Flyer-Design für Zweithaar Studio
Zielgruppe
Firma LORIN Falk ist ein Zweithaar Studio. Hier erhalten Kunden individuell auf sie zugeschnittene Perücken und Toupets. Unsere Zielgruppe sind Männer und Frauen mit wenig oder keiner Kopfbehaarung oder Menschen die krankheitsbedingt unter Haarausfall leiden.
Aufgabenstellung
Bitte Vorschläge zu Anzahl Seiten und Format erstellen, aktuell haben wir noch keine Vorstellung dazu. Folgende Inhalte haben wir schon mal als Entwurf vorbereitet:
Eine Seite zum Thema Toupets mit dem Bild vom Mann:
Leiden Sie an übermäßigem Haarausfall?
Fühlen Sie sich nicht mehr 100% wohl damit und möchten gerne wieder Ihre Attraktivität und vor allem das Wohlbefinden steigern?
Dann sind Sie bei uns sehr gut aufgehoben, denn wir können Ihnen Ihr Toupet individuell auf Ihre Bedürfnisse hin z.B. Farbe, Grauanteil, Größe und Styling anpassen.
Eine Seite zum Thema Perücken mit dem Bild der Frau:
Sind Sie an einer Perücke interessiert die augenscheinlich keinen Unterschied zu gewachsenem Haar aufweist?
Dann sind Sie bei uns an der richtigen Adresse. Die langjährige Erfahrung im Zweithaar Bereich von Friseurmeisterin verspricht Ihnen optimale Beratung und ein individuell auf Sie abgestimmtes Produkt.
Bei uns erhalten Sie Zugriff auf verschiedene Modelle im gesamten Preisspektrum.
Liegt eine von Ihrem Arzt attestierte Erkrankung vor, übernimmt Ihre Krankenkasse höchstwahrscheinlich die Kosten für Ihr Zweithaar. Die Formalitäten dazu erledigen wir gerne für Sie um Ihnen unnötigen Stress zu ersparen.
Eine weitere Seite mit den besonderen Merkmalen mit dem Bild Diversity:
Mit unserer Befestigungsmethode sind Sie sehr flexibel - starker halt für jede Situation und auf Wunsch auch abnehmbar z.B. nachts beim schlafen.
Der große Vorteil unserer Befestigungsmethode liegt darin, dass Sie diese selbst umsetzen können und somit nicht jeden Monat das Studio zur Neubefestigung aufsuchen müssen. Das spart Ihnen Zeit und Geld.
Wir können Ihnen Toupets und Perücken in allen Preisklassen anbieten, in verschiedenen Farben, auf Wunsch mit Grauanteil passend zum Alter des Trägers. Unsere Friseurmeisterin Frau Kessing berät Sie gerne, natürlich unverbindlich und kostenlos.

```html
<!DOCTYPE html>
<html lang="de">
<head>
<meta charset="utf-8">
<title>LORIN Falk – Flyer</title>
<link rel="stylesheet" href="https://fonts.googleapis.com/css2?family=Fira+Sans:wght@600;700&family=Open+Sans:wght@400;600;700&display=swap">
<style>
:root{
  --bg:#ececec;
  --dark:#1f2026;
  --dark-2:#2d2e35;
  --grey:#6f7275;
  --grey-line:#a9abad;
  --tag:#dadada;
  --tag-text:#6b6d70;
  --paper:#f6f6f6;
  --text:#5d5f62;
  --white:#ffffff;
}
*{margin:0;padding:0;box-sizing:border-box}
html,body{width:1200px;height:2350px;overflow:hidden}
body{background:var(--bg);font-family:"Open Sans",Arial,sans-serif;color:var(--text)}
.spread{position:absolute;left:60px;width:1080px;height:764px;display:flex;box-shadow:0 14px 40px rgba(0,0,0,.18)}
.spread--outside{top:331px}
.spread--inside{top:1255px}
.panel{position:relative;width:360px;height:764px;overflow:hidden}
.photo{position:absolute}
.tag{display:inline-block;background:var(--tag);color:var(--tag-text);text-transform:uppercase;letter-spacing:1px;font-size:12px;padding:3px 12px;margin-bottom:4px}
.tag-stack{position:absolute;display:flex;flex-direction:column;align-items:flex-start}
.brand{font-family:"Open Sans",Arial,sans-serif;font-weight:700;letter-spacing:3px;text-align:center;text-transform:uppercase}
.icon{width:18px;height:18px;fill:none;stroke:currentColor;stroke-width:1.6}

/* outside left */
.panel--wig{background:var(--paper)}
.wig__intro{position:absolute;left:26px;top:34px;width:300px;font-weight:700;font-size:11.5px;line-height:1.4}
.wig__list{position:absolute;left:26px;top:150px;width:310px;list-style:none}
.wig__list li{display:flex;gap:14px;font-size:11.5px;line-height:1.45;margin-bottom:18px}
.wig__list svg{flex:none;width:26px;height:26px;color:var(--grey)}
.panel--wig .photo{left:0;bottom:0;width:360px;height:300px;background:linear-gradient(135deg,#2a2b2e,#4a4c52 55%,#1b1c20)}

/* outside contact */
.panel--contact{background:var(--grey);color:var(--white)}
.panel--contact .brand{position:absolute;top:112px;left:0;width:100%;font-size:38px;line-height:1}
.contact__list{position:absolute;top:200px;left:50px;width:260px;list-style:none;text-align:center;font-size:10.5px;line-height:1.45}
.contact__list li{margin-bottom:14px}
.contact__rule{display:flex;align-items:center;gap:10px;margin-bottom:6px}
.contact__rule::before,.contact__rule::after{content:"";flex:1;height:1px;background:var(--grey-line)}
.contact__rule svg{width:14px;height:14px;fill:var(--white);stroke:none}
.hours{position:absolute;left:40px;top:556px;width:280px;border:1.5px solid var(--grey-line);padding:18px 16px 14px;font-size:10.5px}
.hours__title{position:absolute;top:-8px;left:50%;transform:translateX(-50%);background:var(--grey);padding:0 8px;font-weight:700;font-size:10px;letter-spacing:1px}
.hours table{width:100%;border-collapse:collapse}
.hours td{padding:1px 0;vertical-align:top}

/* cover */
.panel--cover{background:linear-gradient(180deg,var(--dark-2),var(--dark) 50%)}
.panel--cover .brand{position:absolute;top:40px;left:0;width:100%;font-size:40px;color:var(--white);line-height:1}
.cover__title{position:absolute;top:118px;left:0;width:100%;text-align:center;font-family:"Fira Sans",Arial,sans-serif;font-weight:700;color:var(--white);font-size:30px;line-height:1.05;text-transform:uppercase}
.cover__title small{font-size:15px;font-weight:600}
.cover__url{position:absolute;top:200px;width:100%;text-align:center;color:var(--white);font-size:11px}
.panel--cover .photo{left:0;top:240px;width:360px;height:524px;background:radial-gradient(ellipse at 50% 45%,#8a2a22 0%,#5a1a16 35%,#231518 70%,var(--dark) 100%)}
.cta{right:22px;bottom:54px;align-items:flex-end}
.cta .tag{font-size:17px;padding:4px 16px;background:rgba(218,218,218,.92)}

/* inside */
.faces{position:absolute;left:0;top:0;width:720px;height:250px;background:linear-gradient(90deg,#6d5245,#c99c82 20%,#8a6a58 40%,#d7b09a 60%,#7b5d4c 80%,#bf9a86);z-index:2}
.panel--toupet{background:var(--paper)}
.questions{position:absolute;left:0;top:270px;width:360px}
.questions p{background:#e7e7e7;margin:0 0 8px;padding:6px 24px;text-transform:uppercase;font-size:13px;letter-spacing:.6px;line-height:1.3}
.questions .tag{margin-left:24px}
.fit{position:absolute;left:0;bottom:0;width:360px;height:200px;background:var(--grey);color:var(--white);padding:22px 24px}
.fit__lead{font-weight:700;font-size:12px;line-height:1.35;margin-bottom:16px}
.fit__grid{display:grid;grid-template-columns:1fr 1fr;gap:14px 10px;list-style:none;font-size:14px;text-transform:uppercase;letter-spacing:1px}
.fit__grid li{display:flex;align-items:center;gap:10px}
.fit__grid svg{width:24px;height:24px;color:var(--white)}
.panel--fix{background:var(--white)}
.panel--fix .tag-stack{left:22px;top:268px}
.fix__text{position:absolute;left:26px;top:340px;width:310px;font-size:11px;line-height:1.45}
.fix__text p{margin-bottom:10px}
.fix__contact{position:absolute;left:26px;top:600px;list-style:none;font-size:13px;font-weight:600}
.fix__contact li{display:flex;gap:10px;align-items:flex-start;margin-bottom:8px}
.fix__contact svg{width:14px;height:14px;fill:var(--grey);margin-top:3px}
.panel--studio{background:var(--white)}
.studio__box{position:absolute;left:22px;top:0;width:318px;height:450px;background:var(--grey);color:var(--white);padding:24px 20px}
.studio__box .tag{margin-bottom:14px}
.studio__box p{font-size:10.5px;line-height:1.45;margin-bottom:9px}
.panel--studio .photo{left:0;bottom:0;width:360px;height:330px;background:linear-gradient(120deg,#e9e4de,#d9c39b 35%,#8a8d92 65%,#3a3b3f)}
</style>
</head>
<body>

<section class="spread spread--outside">
  <article class="panel panel--wig">
    <p class="wig__intro">Sind Sie an einer Perücke interessiert die augenscheinlich keinen Unterschied zu gewachsenem Haar aufweist?</p>
    <div class="tag-stack" style="left:26px;top:88px">
      <span class="tag">Dann sind Sie bei uns an der</span>
      <span class="tag">richtigen Adresse</span>
    </div>
    <ul class="wig__list">
      <li><svg viewBox="0 0 24 24" class="icon"><circle cx="12" cy="9" r="6"/><circle cx="12" cy="9" r="2.5"/><path d="M8 14l-2 8 6-3 6 3-2-8"/></svg><span>Die langjährige Erfahrung im Zweithaar Bereich von Friseurmeisterin Marion Kessing verspricht Ihnen optimale Beratung und ein individuell auf Sie abgestimmtes Produkt.</span></li>
      <li><svg viewBox="0 0 24 24" class="icon"><rect x="2" y="4" width="6" height="16"/><path d="M8 8l5-3 4 12-9 3"/><path d="M14 6l6 2-3 12"/></svg><span>Bei uns erhalten Sie Zugriff auf verschiedene Modelle im gesamten Preisspektrum.</span></li>
      <li><svg viewBox="0 0 24 24" class="icon"><rect x="4" y="3" width="16" height="18" rx="1"/><path d="M8 8h8M8 12h8M8 16h5"/></svg><span>Liegt eine von Ihrem Arzt attestierte Erkrankung vor, übernimmt Ihre Krankenkasse höchstwahrscheinlich die Kosten für Ihr Zweithaar.<br>Die Formalitäten dazu erledigen wir gerne für Sie um Ihnen unnötigen Stress zu ersparen.</span></li>
    </ul>
    <div class="photo" role="img" aria-label="Foto: lächelnder junger Mann in dunkler Jacke vor dunkler Holzwand"></div>
  </article>

  <article class="panel panel--contact">
    <div class="tag-stack" style="left:0;top:22px">
      <span class="tag">Kostenlos und unverbindlich</span>
      <span class="tag">beraten lassen!</span>
    </div>
    <div class="brand">LORIN Falk</div>
    <ul class="contact__list">
      <li><div class="contact__rule"><svg viewBox="0 0 16 16"><circle cx="8" cy="5" r="3"/><path d="M2 15c0-4 3-6 6-6s6 2 6 6z"/></svg></div><b>LORIN Falk | Marion Kessing</b><br>Lindenhofer Straße 7<br>45127 Essen</li>
      <li><div class="contact__rule"><svg viewBox="0 0 16 16"><path d="M4 1l3 3-2 2c1 2 2 3 4 4l2-2 3 3-2 3C6 14 2 10 1 3z"/></svg></div><b>Festnetz:</b> 0201 48 70 26 19<br><b>Mobil:</b> 0172 38 41 905</li>
      <li><div class="contact__rule"><svg viewBox="0 0 16 16"><path d="M1 3h14v10H1z"/><path d="M1 3l7 6 7-6" stroke="#6f7275" stroke-width="1.2" fill="none"/></svg></div><b>EMail:</b> info@lorin-falk.de</li>
      <li><div class="contact__rule"><svg viewBox="0 0 16 16"><circle cx="8" cy="8" r="7"/><path d="M1 8h14M8 1c-3 4-3 10 0 14M8 1c3 4 3 10 0 14" stroke="#6f7275" stroke-width="1" fill="none"/></svg></div><b>www.lorin-falk.de</b></li>
    </ul>
    <div class="hours">
      <span class="hours__title">ÖFFNUNGSZEITEN</span>
      <table>
        <tr><td>Montag:</td><td>geschlossen</td></tr>
        <tr><td>Dienstag - Freitag:</td><td>09:30h - 18:00h</td></tr>
        <tr><td>Samstag:</td><td>nach Terminvereinbarung</td></tr>
      </table>
    </div>
  </article>

  <article class="panel panel--cover">
    <div class="brand">LORIN Falk</div>
    <h1 class="cover__title">Perücken <small>und</small><br>Toupets!</h1>
    <p class="cover__url">www.lorin-falk.de</p>
    <div class="photo" role="img" aria-label="Foto: Frau mit langen roten Haaren vor dunklem Hintergrund"></div>
    <div class="tag-stack cta">
      <span class="tag">Jetzt Termin</span>
      <span class="tag">vereinbaren</span>
    </div>
  </article>
</section>

<section class="spread spread--inside">
  <div class="faces" role="img" aria-label="Fotoreihe: lächelnde Menschen unterschiedlicher Herkunft in schmalen Streifen"></div>
  <article class="panel panel--toupet">
    <div class="questions">
      <p>Leiden Sie an übermäßigem<br>Haarausfall?</p>
      <p>Fühlen Sie sich nicht mehr 100%<br>wohl damit?</p>
      <p>Möchten Sie Ihre Attraktivität<br>und Ihr Wohlbefinden steigern</p>
      <p>Dann sind Sie bei uns</p>
      <span class="tag">Genau richtig!</span>
    </div>
    <div class="fit">
      <p class="fit__lead">Wir passen Ihr Toupet individuell und auf Ihre Bedürfnisse an:</p>
      <ul class="fit__grid">
        <li><svg viewBox="0 0 24 24" class="icon"><rect x="3" y="4" width="5" height="16"/><path d="M8 9l5-3 4 11-9 3"/></svg>Farbe</li>
        <li><svg viewBox="0 0 24 24" class="icon"><path d="M4 12c3-6 10-6 14-2"/><path d="M18 6v4h-4"/><circle cx="9" cy="17" r="3"/></svg>Grauanteil</li>
        <li><svg viewBox="0 0 24 24" class="icon"><rect x="2" y="9" width="20" height="6"/><path d="M6 9v3M10 9v3M14 9v3M18 9v3"/></svg>Größe</li>
        <li><svg viewBox="0 0 24 24" class="icon"><circle cx="6" cy="18" r="3"/><circle cx="18" cy="18" r="3"/><path d="M8 16L18 4M16 16L6 4"/></svg>Styling</li>
      </ul>
    </div>
  </article>

  <article class="panel panel--fix">
    <div class="tag-stack">
      <span class="tag">Befestigung mit maximaler</span>
      <span class="tag">Flexibilität</span>
    </div>
    <div class="fix__text">
      <p>Mit unserer Befestigungsmethode sind Sie sehr flexibel - starker Halt für jede Situation und auf Wunsch auch abnehmbar zum Beispiel nachts beim schlafen.</p>
      <p>Der große Vorteil unserer Befestigungsmethode liegt darin, dass Sie diese selbst umsetzen können und somit nicht jeden Monat das Studio zur Neubefestigung aufsuchen müssen. <b>Das spart Ihnen Zeit und Geld.</b></p>
      <p>Wir können Ihnen Toupets und Perücken in allen Preisklassen anbieten, in verschiedenen Farben, auf Wunsch mit Grauanteil passend zum Alter des Trägers.</p>
      <p>Unsere Friseurmeisterin Frau Kessing berät Sie gerne, natürlich unverbindlich und kostenlos.</p>
    </div>
    <ul class="fix__contact">
      <li><svg viewBox="0 0 16 16"><path d="M4 1l3 3-2 2c1 2 2 3 4 4l2-2 3 3-2 3C6 14 2 10 1 3z"/></svg><span>0201 - 48 70 26 19<br>Mobil: 0172 38 41 905</span></li>
      <li><svg viewBox="0 0 16 16"><path d="M1 3h14v10H1z"/></svg><span>info@lorin-falk.de</span></li>
      <li><svg viewBox="0 0 16 16"><circle cx="8" cy="8" r="7"/></svg><span>www.lorin-falk.de</span></li>
    </ul>
  </article>

  <article class="panel panel--studio">
    <div class="studio__box">
      <span class="tag">Wir beraten Sie gerne!</span>
      <p>Unser Zweithaar Studio befindet sich im ersten Obergeschoss eines barrierefrei zugänglichen Ärztehauses. Es arbeiten mehrere Praxen in dem Gebäude, daher können Sie völlig unauffällig unser Studio erreichen.</p>
      <p>Frau Kessing freut sich Sie in unserem Studio begrüßen zu dürfen.</p>
      <p>Während Ihres Termins sind Sie der einzige Kunde vor Ort, es werden keine Paralleltermine vereinbart. Ein Sichtschutz trennt den Arbeitsbereich vom Eingangsbereich im Studio für den Fall dass spontan ein Kunde z.B. Zubehör abholen möchte.</p>
      <p>Für alle Kunden die mit den öffentlichen Verkehrsmitteln anreisen haben wir auch gute Nachrichten. Die nächste Bahn und U-Bahn Station befinden sich nur 2-3 Gehminuten von uns entfernt.</p>
    </div>
    <div class="photo" role="img" aria-label="Foto: Friseurin schneidet einer blonden Kundin im Salon die Haare"></div>
  </article>
</section>

</body>
</html>
```